Dallas Texas Special Event Center Flyer

Need a new brochure (small 8.5 x 11 tri-fold) for an event center in Dallas, Texas area. It is located on a golf course and is ideal for weddings, quinceaneras, retirement parties, etc. Is best known for weddings. There is no logo for the event center. I have attached the prior brochure, which is not professional. We do not have any site photos.

Target Market(s)

people seeking special event space in dallas, texas area. Brides, meeting planners, etc.

Industry/Entity Type

Golf Course

Font styles to use
Script
Other font styles liked:
• combine serif and some use of script ok

Requirements
Must have
• lots of photos - see attached

```html
<!DOCTYPE html>
<html lang="en">
<head>
<meta charset="utf-8">
<title>Event Center at Willowbend – Tri-fold Brochure</title>
<link href="https://fonts.googleapis.com/css2?family=Cinzel:wght@400;700&family=Raleway:wght@400;700&display=swap" rel="stylesheet">
<style>
:root{
  --stage:#9a9a9a;
  --paper:#ffffff;
  --taupe:#8a7470;
  --taupe-dark:#6f5d59;
  --ink:#4a3f3c;
  --body:#6b6260;
  --cream:#f3ece6;
  --frame:#ffffff;
}
*{margin:0;padding:0;box-sizing:border-box}
html,body{width:1200px;height:1000px;overflow:hidden}
body{background:var(--stage);position:relative;font-family:"Raleway",sans-serif;color:var(--body)}
.spread{position:absolute;left:290px;width:620px;height:480px;background:var(--paper);overflow:hidden;box-shadow:0 2px 6px rgba(0,0,0,.25)}
.spread--outside{top:14px}
.spread--inside{top:505px}
.abs{position:absolute}
.photo{position:absolute;border:3px solid var(--frame)}
.serif{font-family:"Cinzel",serif}

/* outside spread */
.outside-bg{left:0;top:0;width:414px;height:480px;background:linear-gradient(135deg,#f4efec 0%,#e9e0db 40%,#f7f3f1 100%)}
.intro{left:17px;top:30px;width:200px}
.intro h1{font-family:"Cinzel",serif;font-weight:400;font-size:14.5px;line-height:18px;color:var(--ink);letter-spacing:.3px}
.intro p{font-size:8.6px;line-height:11.3px;margin-top:6px}
.intro strong{color:var(--ink);font-weight:700}
.room-title{font-family:"Cinzel",serif;font-size:13px;color:var(--ink);margin-top:9px;line-height:14px}
.room-lead{font-weight:700;color:var(--taupe-dark);font-size:9px;line-height:11px}
.contact{left:223px;top:320px;width:185px;font-size:8.6px;line-height:11px}
.contact .label{margin-top:9px}
.contact .web{font-family:"Cinzel",serif;font-size:8px;color:var(--ink)}
.contact .name{font-family:"Cinzel",serif;font-size:11px;color:var(--ink)}
.contact .venue{font-family:"Cinzel",serif;font-size:10px;color:var(--ink);line-height:12px;margin-top:10px}
.cover{left:414px;top:0;width:206px;height:480px;background:var(--paper)}
.brand{left:0;top:30px;width:206px;text-align:center;font-family:"Cinzel",serif;color:var(--taupe)}
.brand .small{font-size:9.5px;letter-spacing:.5px}
.brand .name{font-size:27px;line-height:30px}
.uses{left:0;top:92px;width:206px;text-align:center;font-family:"Cinzel",serif;font-size:8px;line-height:12px;color:var(--ink)}
.collage-bg{left:0;top:132px;width:206px;height:290px;background:linear-gradient(160deg,#c9a77a,#8f7a52 55%,#6b5a45)}
.cover-band{left:0;top:422px;width:206px;height:58px;background:var(--taupe);color:#fff;font-family:"Cinzel",serif;font-size:10px;line-height:15px;text-align:center;padding-top:6px}

/* inside spread */
.hero{left:0;top:0;width:620px;height:480px;background:linear-gradient(180deg,#2a2220 0%,#5b4a44 30%,#d9d2cf 55%,#f4f1f0 100%)}
.hero-flowers{left:90px;top:20px;width:320px;height:180px;background:radial-gradient(ellipse at center,#e8e0e6 0%,#b8a7b6 45%,rgba(90,110,70,.6) 70%,rgba(0,0,0,0) 100%)}
.location{left:432px;top:18px;width:170px;font-family:"Cinzel",serif;font-size:8.6px;line-height:11.5px;color:#efe7e3;text-align:justify;letter-spacing:.6px}
.band{left:0;top:198px;width:468px;height:83px;background:var(--taupe);color:#fff;font-family:"Cinzel",serif;font-size:11.5px;line-height:20px;text-align:center;padding-top:10px;letter-spacing:.3px}
.band strong{font-weight:700}
.kitchen{left:21px;top:421px;width:375px;font-size:8.6px;line-height:11px;text-align:justify}
.kitchen strong{color:var(--ink)}
</style>
</head>
<body>

<section class="spread spread--outside">
  <div class="abs outside-bg" role="img" aria-label="Soft blurred wedding reception background"></div>

  <div class="abs intro">
    <h1>HOST YOUR EVENT AT THE DALLAS AREA'S PREMIERE EVENT VENUE.</h1>
    <p>The Event Center at Willowbend offers a <strong>12,000 square foot</strong> facility which boasts a Grand Ballroom and two Banquet rooms.</p>
    <div class="room-title">THE GRAND BALLROOM</div>
    <div class="room-lead">will accommodate 809 guests</div>
    <p style="margin-top:0">for a wedding ceremony and reception, quinceanera, retirement party or any occasion that demands a large-scale, elegant setting.</p>
    <p style="margin-top:10px"><strong>The bridal suite</strong> at the top of the winding staircase allows the Bride and her bridesmaids to prepare for the big day out of sight of arriving guests, allowing a dramatic grand entrance.</p>
    <div class="room-title">BANQUET ROOM 1</div>
    <div class="room-lead">will accommodate 103 guests<br>for a mid-size, private event</div>
    <p style="margin-top:0">such as a birthday or retirement party or company holiday party.</p>
    <div class="room-title">BANQUET ROOM 2</div>
    <div class="room-lead">will accommodate 35 guests<br>for a small intimate event</div>
    <p style="margin-top:0">such as a bridal shower, bridesmaid's luncheon or corporate training.</p>
    <p style="margin-top:10px">The rooms can be used separately<br>or together.</p>
  </div>

  <div class="photo" style="left:223px;top:0;width:175px;height:180px;background:linear-gradient(160deg,#f2ede8,#8c7d72 60%,#3a302b)" role="img" aria-label="Bride in a veil"></div>
  <div class="photo" style="left:223px;top:180px;width:175px;height:131px;background:linear-gradient(135deg,#e8d3cf,#f7f1ec 50%,#c9a9a3)" role="img" aria-label="Bridesmaids holding white bouquets"></div>

  <div class="abs contact">
    <p>Contact us for more information<br>or visit us at:</p>
    <p class="label">Website:</p>
    <p class="web">WWW.WILLOWBENDGOLF.COM/EVENTS/</p>
    <p class="label">Contact:</p>
    <p class="name">LENA MARSH</p>
    <p>(214) 555 - 0142 or (972) 555 - 0187<br>Lena.Marsh@willowbendevents.com</p>
    <p class="venue">EVENT CENTER AT WILLOWBEND<br>4810 MEADOW RIDGE ROAD<br>KEMP PARK, TX 75000</p>
  </div>

  <div class="abs cover">
    <div class="abs brand">
      <div class="small">EVENT CENTER AT</div>
      <div class="name">WILLOWBEND</div>
    </div>
    <div class="abs uses">WEDDING | CONFERENCE | SEMINAR | PARTY<br>REUNION | GRADUATION</div>
    <div class="abs collage-bg" role="img" aria-label="Sunlit garden backdrop"></div>
    <div class="photo" style="left:14px;top:159px;width:88px;height:230px;background:linear-gradient(170deg,#d9c3a4,#f2ebe2 55%,#b49a78)" role="img" aria-label="Wedding couple smiling outdoors"></div>
    <div class="photo" style="left:105px;top:129px;width:87px;height:112px;background:linear-gradient(140deg,#c79a6a,#efe2cc 60%,#a77d55)" role="img" aria-label="Guests toasting with champagne"></div>
    <div class="photo" style="left:105px;top:306px;width:87px;height:112px;background:linear-gradient(140deg,#7c8b5a,#f0c8cf 45%,#f4eeee 75%)" role="img" aria-label="Pink and white rose bouquet"></div>
    <div class="abs cover-band">HOST YOUR EVENT AT<br>THE DALLAS AREA'S PREMIERE<br>EVENT VENUE.</div>
  </div>
</section>

<section class="spread spread--inside">
  <div class="abs hero" role="img" aria-label="Table centerpiece of roses and greenery at a reception"></div>
  <div class="abs hero-flowers" role="img" aria-label="Pastel floral arrangement"></div>

  <p class="abs location">THE EVENT CENTER AT WILLOWBEND IS LOCATED ON WILLOWBEND GOLF COURSE, AN 18-HOLE, 215-ACRE CHAMPIONSHIP GOLF COURSE IN KEMP PARK, TEXAS AND IS SURROUNDED BY ROLLING HILLS, SEVEN BEAUTIFUL LAKES, CREEKS, PECAN ORCHARDS AND MANY VARIETIES OF WILDLIFE.</p>

  <div class="abs band"><strong>THE EVENT CENTER AT WILLOWBEND</strong> IS THE PERFECT LOCATION<br>FOR YOUR WEDDING, CONFERENCE, SEMINAR, PARTY,<br>REUNION OR GRADUATION.</div>

  <div class="photo" style="left:468px;top:152px;width:104px;height:103px;background:linear-gradient(150deg,#f6ece8,#e3c9c2 60%,#c99a8e)" role="img" aria-label="Lace wedding gown being fastened"></div>
  <div class="photo" style="left:311px;top:257px;width:102px;height:100px;background:linear-gradient(150deg,#b07550,#e6cfc0 55%,#f4efea)" role="img" aria-label="Bride getting her makeup done"></div>
  <div class="photo" style="left:415px;top:257px;width:101px;height:100px;background:linear-gradient(150deg,#f1e2c6,#c9ab7f 55%,#5e4d3d)" role="img" aria-label="Microphone on a conference stage"></div>
  <div class="photo" style="left:518px;top:257px;width:101px;height:100px;background:linear-gradient(150deg,#fbf2e6,#efd7b5 55%,#d9a88f)" role="img" aria-label="Wedding cake with sugar roses"></div>
  <div class="photo" style="left:470px;top:361px;width:102px;height:100px;background:linear-gradient(150deg,#4a3a36,#f2ece9 50%,#d69aa8)" role="img" aria-label="Cutting a floral wedding cake"></div>

  <p class="abs kitchen">The event center has a <strong>full commercial kitchen onsite</strong> to cater any event from formal dining to buffet-style. The menu can be customized to your specifications and will be prepared by our expert chef and his team.</p>
</section>

</body>
</html>
```